Design a Cover for a Book on Innovation

I need a design for my book: The Quiet Orchard of Tinkering
It is about the following:

Innovation is not just for those endowed with special talent or skills in technology. This book describes the thought framework that consists of seven principal differences between the current period and the past. Innovation is happening along these shifts. Understanding the differences can allow for consistent innovation and the identification of real opportunities.
Updates

To All: All of you show great talent as designers. I've added a bit more to the description. Feel free to ask questions. Best, DT

Font styles to use
Sans Serif

Colors

Designer to choose colors to be used in the design.

Requirements
Must have
• It should feel modern and innovative. It should incorporate the meaning of Quiet Orchard.
Nice to have
• It should have the title, and a holder spot for the subtitle and author's name Dora Teske
Should not have
• It should not be overly busy. Sleek modern design that still gets the point across. Alternatively an image that is a full cover graphic.

```html
<!DOCTYPE html>
<html lang="en">
<head>
<meta charset="utf-8">
<title>The Quiet Orchard of Tinkering — Book Cover</title>
<link rel="stylesheet" href="https://fonts.googleapis.com/css2?family=Jost:wght@400;500&display=swap">
<style>
  :root {
    --backdrop: #d4d4d4;
    --cover: #ffffff;
    --ink-blue: #17508c;
    --ink-dark: #111111;
    --rule-blue: #1d4f86;
    --art-warm: #f3e36a;
    --art-cool: #6fb7e8;
    --art-violet: #a46ad8;
  }
  * { margin: 0; padding: 0; box-sizing: border-box; }
  html, body {
    width: 1200px;
    height: 900px;
    overflow: hidden;
    background: var(--backdrop);
    font-family: "Jost", "Futura", sans-serif;
  }
  .canvas {
    position: relative;
    width: 1200px;
    height: 900px;
    background: var(--backdrop);
  }
  .book-cover {
    position: absolute;
    left: 318px;
    top: 0;
    width: 635px;
    height: 897px;
    background: var(--cover);
  }
  .title {
    position: absolute;
    left: 0;
    top: 96px;
    width: 100%;
    text-align: center;
    color: var(--ink-blue);
  }
  .title-ruled {
    display: flex;
    align-items: center;
    justify-content: center;
    gap: 10px;
    font-size: 24px;
    font-weight: 400;
    letter-spacing: 5px;
    color: var(--ink-dark);
    line-height: 1;
  }
  .title-ruled::before,
  .title-ruled::after {
    content: "";
    display: block;
    width: 112px;
    height: 2px;
    background: linear-gradient(90deg, rgba(29,79,134,0), var(--rule-blue));
  }
  .title-ruled::after {
    background: linear-gradient(90deg, var(--rule-blue), rgba(29,79,134,0));
  }
  .title-major {
    display: block;
    font-weight: 400;
    line-height: 1;
    color: var(--ink-blue);
  }
  .title-major--first {
    font-size: 88px;
    letter-spacing: 1px;
    margin-top: 12px;
    margin-bottom: 14px;
  }
  .title-major--second {
    font-size: 72px;
    letter-spacing: 0;
    margin-top: 12px;
  }
  .cover-art {
    position: absolute;
    left: 100px;
    top: 398px;
    width: 470px;
    height: 180px;
    border-radius: 6px;
    background:
      radial-gradient(circle at 85% 45%, var(--art-warm) 0, rgba(243,227,106,0) 32%),
      linear-gradient(90deg, #f4eeee 0%, #e6f2fb 30%, #f5ece2 48%, #efe6f8 62%, #e7f6e9 76%, #fbf7e2 100%);
  }
  .tagline-block {
    position: absolute;
    left: 0;
    top: 646px;
    width: 100%;
    text-align: center;
  }
  .tagline-rule {
    display: block;
    width: 370px;
    height: 2px;
    margin: 0 auto;
    background: linear-gradient(90deg, rgba(29,79,134,0), var(--rule-blue) 30%, var(--rule-blue) 70%, rgba(29,79,134,0));
  }
  .tagline {
    margin: 11px auto 20px;
    width: 560px;
    font-size: 14.2px;
    font-weight: 500;
    line-height: 1.45;
    color: var(--ink-dark);
  }
  .author {
    position: absolute;
    left: 0;
    top: 794px;
    width: 100%;
    text-align: center;
    font-size: 26px;
    font-weight: 400;
    letter-spacing: 6px;
    color: var(--ink-dark);
  }
</style>
</head>
<body>
  <div class="canvas">
    <section class="book-cover">
      <h1 class="title">
        <span class="title-ruled">THE QUIET</span>
        <span class="title-major title-major--first">ORCHARD</span>
        <span class="title-ruled">OF</span>
        <span class="title-major title-major--second">TINKERING</span>
      </h1>

      <div class="cover-art" role="img" aria-label="A row of colourful crumpled paper balls leading to a yellow crumpled-paper light bulb with sketched arrows bursting outward"></div>

      <div class="tagline-block">
        <span class="tagline-rule"></span>
        <p class="tagline">Innovation is happening along these shifts. Understanding the differences can allow for consistent innovation and the identification of real opportunities.</p>
        <span class="tagline-rule"></span>
      </div>

      <p class="author">DORA TESKE</p>
    </section>
  </div>
</body>
</html>
```